Larkfield Clinic Marketing Flyer

We are a new medical practice in the community and need a flyer to send to other medical offices to inform of our services. We just completed our logo with PixelGuild and would like to incorporate that plus our marketing content into the flyer. Our medical practice has 2 divisions: (1)Mental Health/Psychiatry and (2) Migraine and Neurospasticity Management. Please see website for content and provider photos at www.LarkfieldCare.example

Target Market(s)

Other Healthcare Professionals in the Community

Industry/Entity Type

Medical

Requirements
Must have
• Photos of all 5 healthcare providers, phone number, address, logo

```html
<!DOCTYPE html>
<html lang="en">
<head>
<meta charset="utf-8">
<title>Larkfield Clinic – Flyer</title>
<link href="https://fonts.googleapis.com/css2?family=Montserrat:wght@400;500;600;700&display=swap" rel="stylesheet">
<style>
  :root {
    --mat: #858689;
    --frame: #d0d1d3;
    --paper: #ffffff;
    --soft-grey: #d1d2d4;
    --teal: #1b9688;
    --green: #a6cf52;
    --ink: #111111;
    --body-ink: #222222;
  }
  * { margin: 0; padding: 0; box-sizing: border-box; }
  html, body { width: 871px; height: 1200px; overflow: hidden; }
  body { position: relative; background: var(--mat); font-family: "Montserrat", sans-serif; }
  .abs { position: absolute; }
  .frame { left: 76px; top: 77px; width: 719px; height: 1009px; background: var(--frame); }
  .paper { left: 88px; top: 90px; width: 695px; height: 984px; background: var(--paper); }
  .shapes { left: 0; top: 0; width: 871px; height: 1200px; }

  .brand-name { left: 112px; top: 210px; width: 212px; text-align: center; color: var(--teal); font-weight: 600; font-size: 22px; letter-spacing: 0.5px; }

  .headline { left: 112px; top: 306px; font-weight: 600; font-size: 43px; line-height: 43px; color: var(--ink); }
  .headline.teal { top: 401px; color: var(--teal); }

  .intro { left: 112px; top: 652px; width: 645px; font-size: 11.6px; line-height: 18px; color: var(--body-ink); text-align: justify; font-weight: 500; }

  .panel-head { background: var(--teal); height: 77px; top: 714px; }
  .providers-head { left: 88px; width: 397px; border-top-right-radius: 10px; }
  .intervention-head { left: 499px; width: 284px; border-top-left-radius: 10px; }
  .panel-body { background: var(--green); top: 791px; height: 201px; }
  .providers-body { left: 88px; width: 388px; border-bottom-right-radius: 14px; }
  .intervention-body { left: 510px; width: 273px; border-bottom-left-radius: 14px; }

  .head-title { font-weight: 700; font-size: 19.5px; line-height: 22px; color: #fff; }
  .head-title .lime { color: var(--green); }
  .providers-title { left: 112px; top: 719px; }
  .intervention-title { left: 560px; top: 719px; width: 201px; text-align: right; }

  .headshot { width: 62px; height: 66px; background: #fff; padding: 3px; }
  .headshot div { width: 100%; height: 100%; background: linear-gradient(160deg, #6b7a7e, #2f3a3e); }
  .provider { font-weight: 600; font-size: 10.5px; line-height: 14.5px; color: #fff; white-space: nowrap; }

  .service-text { left: 530px; top: 803px; width: 232px; font-size: 8.3px; line-height: 11.7px; color: var(--body-ink); text-align: justify; }
  .doc-photo { left: 530px; top: 884px; width: 73px; height: 83px; background: #fff; padding: 3px; }
  .doc-photo div { width: 100%; height: 100%; background: linear-gradient(160deg, #8a6a4a, #d9d3c8); }
  .doc-box { left: 605px; top: 884px; width: 178px; height: 83px; background: var(--teal); }
  .doc-text { left: 611px; top: 893px; width: 151px; font-size: 5.9px; line-height: 9.5px; color: #fff; font-weight: 600; text-align: justify; }

  .footer-name { left: 160px; top: 1004px; font-weight: 700; font-size: 19px; line-height: 22px; color: var(--teal); }
  .divider { top: 1005px; width: 1px; height: 44px; background: var(--teal); }
  .address { left: 297px; top: 1011px; width: 152px; text-align: center; font-size: 10.4px; line-height: 18px; color: var(--ink); font-weight: 500; white-space: nowrap; }
  .phone { left: 459px; top: 1010px; font-weight: 500; font-size: 34.5px; line-height: 44px; color: var(--green); white-space: nowrap; }
</style>
</head>
<body>
  <div class="abs frame"></div>
  <div class="abs paper"></div>

  <svg class="abs shapes" viewBox="0 0 1554 2140" xmlns="http://www.w3.org/2000/svg">
    <defs>
      <clipPath id="paper-clip"><rect x="157" y="160" width="1240" height="1755"/></clipPath>
      <linearGradient id="portrait-tone" x1="0" y1="0" x2="0.6" y2="1">
        <stop offset="0" stop-color="#eeeff1"/>
        <stop offset="0.35" stop-color="#e2e3e6"/>
        <stop offset="0.6" stop-color="#b98457"/>
        <stop offset="1" stop-color="#9c5d27"/>
      </linearGradient>
      <linearGradient id="care-tone" x1="0" y1="0" x2="0" y2="1">
        <stop offset="0" stop-color="#e8e6e3"/>
        <stop offset="1" stop-color="#3b4656"/>
      </linearGradient>
    </defs>
    <g clip-path="url(#paper-clip)">
      <path role="img" aria-label="Photo: smiling young woman with curly hair, eyes closed, relaxed" d="M600 160 H1397 V1000 Q1100 1160 620 1080 L600 160 Z" fill="url(#portrait-tone)"/>
      <circle cx="420" cy="600" r="520" fill="var(--soft-grey)" stroke="var(--green)" stroke-width="6"/>
      <circle cx="400" cy="230" r="300" fill="#fff" stroke="var(--green)" stroke-width="5"/>
    </g>
    <circle cx="385" cy="268" r="52" fill="var(--teal)"/>
    <circle role="img" aria-label="Photo: patient with headache consulting a clinician" cx="290" cy="1045" r="100" fill="url(#care-tone)" stroke="var(--green)" stroke-width="13"/>
    <circle role="img" aria-label="Photo: doctors fitting an EEG cap on a patient" cx="533" cy="1045" r="100" fill="url(#care-tone)" stroke="var(--green)" stroke-width="13"/>
  </svg>

  <div class="abs brand-name">Larkfield Clinic</div>

  <div class="abs headline">Mental Health<br>and Psychiatry</div>
  <div class="abs headline teal">Migraine and<br>Neurospasticity</div>

  <p class="abs intro">Bringing comprehensive evaluation, medication management and psychotherapy to the full spectrum of mental health disorders including minor, moderate and major depression, bipolar disorder, ADD/ADHD, anxiety, schizophrenia, stress or grief reactions, and others.</p>

  <div class="abs panel-head providers-head"></div>
  <div class="abs panel-head intervention-head"></div>
  <div class="abs panel-body providers-body"></div>
  <div class="abs panel-body intervention-body"></div>

  <svg class="abs shapes" viewBox="0 0 1554 2140" xmlns="http://www.w3.org/2000/svg">
    <g fill="none" stroke="var(--teal)" stroke-width="2.5">
      <path d="M315 1542 H485 L502 1512"/>
      <path d="M650 1542 H800 L817 1512"/>
      <path d="M315 1710 H475 L492 1680"/>
      <path d="M650 1710 H800 L817 1680"/>
    </g>
  </svg>

  <div class="abs head-title providers-title"><span class="lime">Meet Our</span><br>Mental Health<br><span class="lime">Providers</span></div>
  <div class="abs head-title intervention-title">Migraine and<br><span class="lime">Neurospasticity</span><br>Intervention</div>

  <div class="abs headshot" style="left:110px;top:813px"><div role="img" aria-label="Headshot of provider Milo Haversen"></div></div>
  <div class="abs provider" style="left:181px;top:820px">Milo Haversen,<br>Teens/Adults<br>PMHNP - BC</div>
  <div class="abs headshot" style="left:294px;top:813px"><div role="img" aria-label="Headshot of provider Reed Calloway"></div></div>
  <div class="abs provider" style="left:369px;top:820px">Reed Calloway<br>Peds/Adolescents<br>PMHNP - BC</div>
  <div class="abs headshot" style="left:110px;top:906px"><div role="img" aria-label="Headshot of provider Sheila Brandt"></div></div>
  <div class="abs provider" style="left:181px;top:913px">Sheila Brandt,<br>Teens/Adults<br>PMHNP - BC</div>
  <div class="abs headshot" style="left:294px;top:906px"><div role="img" aria-label="Headshot of provider Joan Whitcombe"></div></div>
  <div class="abs provider" style="left:369px;top:913px">Joan Whitcombe,<br>Adults/Geriatrics<br>PMHNP-BC</div>

  <p class="abs service-text">Injections of botulinum neurotoxin are a widely used therapeutic form of treatment for both chronic migraines and patients with involuntary muscle contractions (neurospasticity). Injections may offer up to 3 months of relief and may be combined with other pharmaceutical interventions for maximum benefit.</p>

  <div class="abs doc-photo"><div role="img" aria-label="Photo of physician Dr. Colin Marsh"></div></div>
  <div class="abs doc-box"></div>
  <p class="abs doc-text">A board certified family practice physician, Dr. Colin Marsh has incorporated botulinum toxin injections into his practice for several years. Now retired from family medicine, he is devoted to helping patients find relief from migraines and muscle spasticity issues.</p>

  <div class="abs footer-name">Larkfield<br>Clinic, pllc</div>
  <div class="abs divider" style="left:295px"></div>
  <div class="abs address">512 N. Aspenwood, Suite B<br>Harbor Falls, ID 83900</div>
  <div class="abs divider" style="left:451px"></div>
  <div class="abs phone">(208)555-0147</div>
</body>
</html>
```